Bramblewick Gardening Services. A6 flyer single sided

Need an A6 flyer designing. Single sided.
I am a gardener.
I do lawn mowing - one-off garden tidy ups or regular fortnightly visits.
All kinds of trees expertly felled, topped or pruned.
Hedge cutting.
Fencing replaced or repaired.
Fully insured.
Access to fully qualified and licenced tree arborist
07724 316048 or 01632 742918.

I have attached my business card and letter head logo.
I'm open to new designs without incorporating any of my artwork.

Industry/Entity Type

Gardener

```html
<!DOCTYPE html>
<html lang="en">
<head>
<meta charset="utf-8">
<title>Bramblewick Garden Services</title>
<link href="https://fonts.googleapis.com/css2?family=Fira+Sans:wght@400;600;800&display=swap" rel="stylesheet">
<style>
  :root {
    --grass-light: #5fae2e;
    --grass-mid: #4a9a22;
    --grass-dark: #3a8419;
    --headline-yellow: #f3e600;
    --panel-lime: #d3d71f;
    --panel-ink: #1d1d0f;
  }
  html, body {
    margin: 0;
    padding: 0;
    width: 1200px;
    height: 846px;
    overflow: hidden;
    background: #ffffff;
  }
  .flyer {
    position: relative;
    width: 1200px;
    height: 846px;
    overflow: hidden;
    font-family: "Fira Sans", Arial, sans-serif;
  }
  .lawn-backdrop {
    position: absolute;
    inset: 0;
    background:
      radial-gradient(ellipse at 40% 35%, var(--grass-light) 0%, transparent 65%),
      linear-gradient(160deg, var(--grass-mid) 0%, var(--grass-light) 45%, var(--grass-dark) 100%);
  }
  .brand {
    position: absolute;
    left: 70px;
    top: 62px;
    color: var(--headline-yellow);
  }
  .brand-name {
    margin: 0;
    font-weight: 800;
    font-size: 86px;
    line-height: 1;
    letter-spacing: -0.5px;
  }
  .brand-tagline {
    margin: 6px 0 0 2px;
    font-weight: 400;
    font-size: 52px;
    line-height: 1.1;
  }
  .contact-panel {
    position: absolute;
    left: 779px;
    top: 68px;
    width: 421px;
    height: 373px;
    background: var(--panel-lime);
    color: var(--panel-ink);
    box-sizing: border-box;
    padding: 24px 0 0 29px;
  }
  .phone {
    display: block;
    font-size: 41px;
    line-height: 58px;
    font-weight: 400;
  }
  .email {
    display: block;
    font-size: 26px;
    line-height: 36px;
    margin-top: -2px;
  }
  .address {
    font-style: normal;
    font-size: 27px;
    line-height: 38px;
    margin-top: 50px;
  }
  .services {
    position: absolute;
    left: 70px;
    top: 464px;
    margin: 0;
    padding: 0;
    list-style: none;
    color: var(--headline-yellow);
    font-weight: 600;
    font-size: 33px;
    line-height: 48.6px;
  }
</style>
</head>
<body>
  <main class="flyer">
    <div class="lawn-backdrop" role="img" aria-label="Aerial photo of a freshly mown green lawn with a gardener pushing a yellow lawnmower"></div>

    <header class="brand">
      <h1 class="brand-name">Bramblewick</h1>
      <p class="brand-tagline">Garden Services</p>
    </header>

    <aside class="contact-panel">
      <span class="phone">01632 742 918</span>
      <span class="phone">07724 316048</span>
      <span class="email">hello@bramblewick-gardens.co.uk</span>
      <address class="address">
        14 Fernhollow Lane<br>
        Oakridge Vale Westmere<br>
        WM4 7QT
      </address>
    </aside>

    <ul class="services">
      <li>Lawn mowing</li>
      <li>Hedge cutting</li>
      <li>Fencing replaced or repaired</li>
      <li>Trees expertly felled, topped or pruned</li>
      <li>One-off garden tidy ups /regular fortnightly visits.</li>
      <li>Access to fully qualified and licenced tree arborist</li>
      <li>Fully insured</li>
    </ul>
  </main>
</body>
</html>
```